Business Card and Letterhead for new company Vardel GreenWorks, Inc.

Vardel GreenWorks, Inc., an engineering and construction firm that provides services for solid waste landfill gas systems, needs a business card and letterhead. We recently had a logo designed but we are open to some tweaks to logo design and color scheme. Generally, we like "earthy" color tones - greens, browns, oranges. This is a sister company - www.talvoriengineering.example.

Target Market(s)

Solid waste landfill companies - Brindle Disposal, Halcott Hauling, etc.

Industry/Entity Type

Engineering and Construction

Contact Information for Business Card

Name, Title, email, mobile phone, work phone, website. Potential list of services for back of card: LFG Engineering and Design, GCCS Planning and Operational Consulting, Compliance Monitoring and Reporting, Routine Operations & Maintenance, Nonroutine O&M, Construction Management, Construction QA, GCCS Construction

Font styles to use
Sans Serif

Requirements
Must have
• Logo, pertinent information, maybe a tagline (still in development)
Nice to have
• For back of card, considering an engineering scale (attached for another business of ours), but want to look at other options, alternatives. Like the idea of the back of card to have some utility (scale, unit conversion info, list of services) but willing to consider lots of options.
Should not have
• Needs to have a professional (engineering) and technical look, not cartoonish.

```html
<!DOCTYPE html>
<html lang="en">
<head>
<meta charset="utf-8">
<title>Vardel GreenWorks – Business Card</title>
<link rel="stylesheet" href="https://fonts.googleapis.com/css2?family=Lato:wght@400;700&display=swap">
<style>
  :root {
    --green: #7ab93c;
    --teal: #3497b4;
    --grey: #8c8d91;
    --ink: #4a4a4c;
    --orange: #f36c21;
    --paper: #ffffff;
    --backdrop: #e9e6e1;
    --faint-teal: #e6f1f5;
  }
  * { box-sizing: border-box; margin: 0; padding: 0; }
  html, body { width: 1200px; height: 780px; overflow: hidden; }
  body {
    background: var(--backdrop);
    font-family: "Lato", sans-serif;
    display: flex;
    align-items: center;
    justify-content: center;
    gap: 40px;
  }
  .card {
    position: relative;
    width: 520px;
    height: 297px;
    background: var(--paper);
    box-shadow: 0 6px 18px rgba(0,0,0,.18);
    overflow: hidden;
  }
  .brand {
    position: absolute;
    display: flex;
    align-items: center;
    gap: 8px;
  }
  .brand-dot {
    width: 14px; height: 14px;
    border-radius: 50%;
    background: var(--green);
    flex: none;
  }
  .brand-name {
    font-weight: 700;
    color: var(--green);
    letter-spacing: .5px;
  }

  /* Front */
  .front-tab {
    position: absolute;
    left: 34px; top: 0;
    width: 30px; height: 6px;
    background: var(--orange);
  }
  .front .brand { left: 34px; top: 26px; }
  .front .brand-name { font-size: 25px; }
  .person { position: absolute; left: 34px; top: 74px; }
  .person-name {
    font-weight: 700;
    font-size: 21px;
    color: var(--green);
    letter-spacing: .5px;
    text-transform: uppercase;
  }
  .person-title { font-size: 13px; color: var(--teal); margin-top: 3px; }
  .contact {
    position: absolute;
    left: 34px; top: 136px;
    list-style: none;
    font-size: 11px;
    color: var(--ink);
    line-height: 1.55;
  }
  .contact li { display: flex; align-items: flex-start; gap: 8px; }
  .contact svg { width: 10px; height: 10px; margin-top: 3px; flex: none; fill: var(--teal); }
  .contact .spacer { width: 10px; flex: none; }
  .company { font-weight: 700; }
  .front-mark {
    position: absolute;
    right: 30px; bottom: 30px;
    width: 150px; height: 150px;
    border-radius: 50%;
    background: var(--teal);
  }

  /* Back */
  .back .brand { left: 30px; top: 26px; }
  .back .brand-name { font-size: 17px; }
  .services {
    position: absolute;
    left: 30px; top: 78px;
    list-style: none;
    font-size: 11.5px;
    color: var(--ink);
    line-height: 1.62;
  }
  .services li { display: flex; align-items: center; gap: 8px; }
  .services svg { width: 10px; height: 10px; flex: none; }
  .back-mark {
    position: absolute;
    right: 34px; bottom: 30px;
    width: 170px; height: 170px;
    border-radius: 50%;
    background: var(--faint-teal);
  }
</style>
</head>
<body>

<svg width="0" height="0" style="position:absolute" aria-hidden="true">
  <defs>
    <symbol id="icon-tick" viewBox="0 0 10 10">
      <circle cx="5" cy="5" r="5" fill="#3497b4"/>
      <path d="M2.8 5.1 L4.4 6.6 L7.3 3.6" fill="none" stroke="#fff" stroke-width="1.3" stroke-linecap="round" stroke-linejoin="round"/>
    </symbol>
  </defs>
</svg>

<section class="card front" aria-label="Business card front">
  <div class="front-tab"></div>
  <div class="brand">
    <span class="brand-dot"></span>
    <span class="brand-name">Vardel GreenWorks</span>
  </div>
  <div class="person">
    <p class="person-name">Daniel Orwick</p>
    <p class="person-title">Founder &amp; CEO</p>
  </div>
  <ul class="contact">
    <li>
      <svg viewBox="0 0 10 10"><path d="M5 0a3.5 3.5 0 0 0-3.5 3.5C1.5 6 5 10 5 10s3.5-4 3.5-6.5A3.5 3.5 0 0 0 5 0zm0 5a1.5 1.5 0 1 1 0-3 1.5 1.5 0 0 1 0 3z"/></svg>
      <span><span class="company">Vardel GreenWorks, Inc.</span><br>423 Street Address Here, City<br>State &amp; Country, ZIP Code</span>
    </li>
    <li>
      <svg viewBox="0 0 10 10"><path d="M2 0.5 L3.6 0.5 L4.3 2.7 L3.2 3.6 C3.8 5 5 6.2 6.4 6.8 L7.3 5.7 L9.5 6.4 L9.5 8 C9.5 8.8 8.8 9.5 8 9.5 C4 9.3 0.7 6 0.5 2 C0.5 1.2 1.2 0.5 2 0.5Z"/></svg>
      <span>(555) 201-4830</span>
    </li>
    <li>
      <svg viewBox="0 0 10 10"><rect x="2.5" y="0.5" width="5" height="9" rx="1" fill="none" stroke="#3497b4" stroke-width="1"/></svg>
      <span>(555) 201-4831</span>
    </li>
    <li>
      <svg viewBox="0 0 10 10"><rect x="0.5" y="2" width="9" height="6" rx="0.8"/><path d="M0.8 2.4 L5 5.5 L9.2 2.4" fill="none" stroke="#fff" stroke-width="0.8"/></svg>
      <span>info@vardelgreenworks.example</span>
    </li>
    <li>
      <svg viewBox="0 0 10 10"><circle cx="5" cy="5" r="4.5" fill="none" stroke="#3497b4" stroke-width="1"/><path d="M0.5 5h9M5 0.5c-2 2.5-2 6.5 0 9M5 0.5c2 2.5 2 6.5 0 9" fill="none" stroke="#3497b4" stroke-width="0.8"/></svg>
      <span>vardelgreenworks.example</span>
    </li>
  </ul>
  <div class="front-mark"></div>
</section>

<section class="card back" aria-label="Business card back">
  <div class="brand">
    <span class="brand-dot"></span>
    <span class="brand-name">Vardel GreenWorks</span>
  </div>
  <div class="back-mark"></div>
  <ul class="services">
    <li><svg><use href="#icon-tick"/></svg>LFG Engineering &amp; Design</li>
    <li><svg><use href="#icon-tick"/></svg>GCCS Planning &amp; Operational Consulting</li>
    <li><svg><use href="#icon-tick"/></svg>Compliance Monitoring &amp; Reporting</li>
    <li><svg><use href="#icon-tick"/></svg>Routine Operations &amp; Maintenance</li>
    <li><svg><use href="#icon-tick"/></svg>Nonroutine O&amp;M</li>
    <li><svg><use href="#icon-tick"/></svg>Construction Management</li>
    <li><svg><use href="#icon-tick"/></svg>Construction QA</li>
    <li><svg><use href="#icon-tick"/></svg>GCCS Construction</li>
  </ul>
</section>

</body>
</html>
```